Solar Company Bussiness Card

I need a 2 sided business card and would like a .psd and any font files for each side of the card. I would like my logo used, it should be attached with the fonts. I'm not opposed to the font colors with the logo being changed.

On the sample design, I'd like the following:

Darren Pellow
President
Phone: 555-318-2947
www.sunvaleenergyco.example

As I've recently opened in a 2nd market, I'm not sure about an address as I currently have 2 of them. I may actually get separate cards printed, one batch for each address, that's why I need the PSD file.
Updates

I'm very pleased with the response and designs I've received here for my business card. First and foremost, I'd like to thank everyone who took the time to submit a design. There truly are a lot of great designs in the bunch here and I'm having a little difficulty deciding. I will be reaching out to someone in the next day or two here to go to a final design. At this time, I'm not looking for any new concepts. If any of you do logos, I'm looking for a new logo for our sister entity, Pellow Partners, Inc. Thanks, Darren Pellow

Reason: I'm not looking for any new designs at this point, but extending this deadline in order to give people I've asked a chance to re-submit items.

Industry/Entity Type

Business

```html
<!DOCTYPE html>
<html lang="en">
<head>
<meta charset="utf-8">
<title>Sunvale Energy – Business Card</title>
<link href="https://fonts.googleapis.com/css2?family=Ubuntu:wght@300;400;500&display=swap" rel="stylesheet">
<style>
  :root {
    --page: #e8e5e0;
    --card-dark: #232324;
    --card-light: #eeeeef;
    --brand-blue: #1d5fa8;
    --sky-blue: #3aa3de;
    --ink: #2b2b2b;
    --text-font: "Ubuntu", sans-serif;
  }
  * { margin: 0; padding: 0; box-sizing: border-box; }
  html, body {
    width: 1200px; height: 1023px; overflow: hidden;
    background: var(--page);
    font-family: var(--text-font);
  }
  .sheet {
    width: 1200px; height: 1023px;
    display: flex; flex-direction: column; align-items: center; justify-content: center;
    gap: 40px;
  }
  .card {
    position: relative;
    width: 840px; height: 480px;
    overflow: hidden;
    box-shadow: 0 6px 18px rgba(0,0,0,.18);
  }
  .brand-name { white-space: nowrap; }

  /* Back side */
  .card-back { background: var(--card-dark); }
  .card-back .brand {
    position: absolute; left: 100px; top: 160px;
    display: flex; align-items: center; gap: 26px;
  }
  .card-back .brand-square {
    width: 96px; height: 96px; background: var(--sky-blue); flex: none;
  }
  .card-back .brand-name {
    font-size: 70px; font-weight: 400; color: var(--brand-blue);
    letter-spacing: 1px; line-height: 1;
  }
  .card-back .tagline {
    position: absolute; right: 90px; top: 290px;
    font-size: 24px; font-weight: 300; color: var(--sky-blue);
    white-space: nowrap;
  }

  /* Front side */
  .card-front { background: var(--card-light); }
  .card-front .brand {
    position: absolute; left: 60px; top: 52px;
    display: flex; align-items: center; gap: 16px;
  }
  .card-front .brand-square { width: 54px; height: 54px; background: var(--sky-blue); flex: none; }
  .card-front .brand-name {
    font-size: 54px; font-weight: 400; color: var(--brand-blue); line-height: 1;
  }
  .person { position: absolute; left: 60px; top: 170px; }
  .person-name { font-size: 34px; font-weight: 400; color: var(--brand-blue); }
  .person-title { font-size: 21px; font-weight: 400; color: var(--ink); margin-top: 4px; }
  .contact { position: absolute; left: 60px; top: 300px; list-style: none; }
  .contact li {
    display: flex; align-items: center; gap: 12px;
    font-size: 21px; color: var(--ink); margin-bottom: 10px; white-space: nowrap;
  }
  .contact svg { width: 18px; height: 18px; fill: var(--brand-blue); flex: none; }
  .address {
    position: absolute; right: 140px; top: 320px; text-align: right;
    font-size: 21px; color: var(--ink); line-height: 1.35; white-space: nowrap;
  }
  .accent-bands { position: absolute; left: 0; bottom: 0; width: 360px; }
  .accent-bands .band-dark { height: 22px; background: var(--brand-blue); }
  .accent-bands .band-light { height: 22px; background: var(--sky-blue); }
  .corner-square {
    position: absolute; right: 36px; bottom: 30px;
    width: 70px; height: 70px; background: var(--sky-blue);
  }
</style>
</head>
<body>
<main class="sheet">
  <section class="card card-back" aria-label="Card back">
    <div class="brand">
      <span class="brand-square"></span>
      <span class="brand-name">Sunvale Energy</span>
    </div>
    <p class="tagline">Powering energy independence.</p>
  </section>

  <section class="card card-front" aria-label="Card front">
    <div class="brand">
      <span class="brand-square"></span>
      <span class="brand-name">Sunvale Energy</span>
    </div>
    <div class="person">
      <p class="person-name">Darren Pellow</p>
      <p class="person-title">President</p>
    </div>
    <ul class="contact">
      <li>
        <svg viewBox="0 0 24 24" aria-hidden="true"><path d="M6.6 10.8a15.1 15.1 0 0 0 6.6 6.6l2.2-2.2c.3-.3.7-.4 1-.2 1.1.4 2.3.6 3.6.6.6 0 1 .4 1 1V20c0 .6-.4 1-1 1A17 17 0 0 1 3 4c0-.6.4-1 1-1h3.5c.6 0 1 .4 1 1 0 1.3.2 2.5.6 3.6.1.3 0 .7-.2 1z"/></svg>
        555-318-2947
      </li>
      <li>
        <svg viewBox="0 0 24 24" aria-hidden="true"><path d="M12 2a10 10 0 1 0 0 20 10 10 0 0 0 0-20zm6.9 6h-3a15.7 15.7 0 0 0-1.4-3.6A8 8 0 0 1 18.9 8zM12 4c.8 1.2 1.5 2.5 1.9 4h-3.8c.4-1.5 1.1-2.8 1.9-4zM4.3 14a8.2 8.2 0 0 1 0-4h3.4a16.5 16.5 0 0 0 0 4zm.8 2h3a15.7 15.7 0 0 0 1.4 3.6A8 8 0 0 1 5.1 16zm3-8h-3a8 8 0 0 1 4.4-3.6C8.900 5.5 8.4 6.7 8.1 8zM12 20c-.8-1.2-1.5-2.5-1.9-4h3.8c-.4 1.5-1.1 2.8-1.9 4zm2.3-6H9.7a14.7 14.7 0 0 1 0-4h4.6a14.7 14.7 0 0 1 0 4zm.3 5.6c.6-1.1 1.1-2.3 1.4-3.6h3a8 8 0 0 1-4.4 3.6zm1.7-5.6a16.5 16.5 0 0 0 0-4h3.4a8.2 8.2 0 0 1 0 4z"/></svg>
        www.sunvaleenergyco.example
      </li>
    </ul>
    <p class="address">Orchard Ln, Millbrook Falls,<br>PA, 17000 United States</p>
    <div class="accent-bands" aria-hidden="true">
      <div class="band-dark"></div>
      <div class="band-light"></div>
    </div>
    <span class="corner-square" aria-hidden="true"></span>
  </section>
</main>
</body>
</html>
```